Tidewell Metrics Group Company Website Design and Coding

We want to redesign our existing website so that it is more visually and functionally appealing to prospective clients and potential job candidates. We would like to keep our current color scheme and implement our current logo as well. We have a high-level idea of website structure that we are thinking of, which is in the attached files. Logo is included as well. The final design would ideally be energy and analytics focused. We will need the new website to be coded as well, please.

Target Market(s)

Energy and utility industry

Industry/Entity Type

Energy/analytics

Coding

Coded - Design and coding required

Number of Pages Required

5+ page

Font styles to use
Sans Serif

Colors
0094D4
00A9DD
6FCCEA
C7EBF8
E9F6FB
F0912C
F2A743
F7CA91
FBE8D2
FDF5EE

Requirements
Must have
• Consistent color scheme- please use the one that we provided. We need an overview, a home page, and our core services. A separate job application page. Logo must be incorporated. We would like e "Meet our Team" page. Please include all of the content that is listed in our attachments.
Nice to have
• Movement
Should not have
• No music, no cartoons/animation, no pictures of a chalkboard

```html
<!DOCTYPE html>
<html lang="en">
<head>
<meta charset="utf-8">
<title>Tidewell Metrics Group – Home Page Variations</title>
<link rel="stylesheet" href="https://fonts.googleapis.com/css2?family=Open+Sans:wght@400;600;700&family=Rajdhani:wght@500;600;700&display=swap">
<style>
:root{
  --blue:#0094D4;--blue2:#00A9DD;--sky:#6FCCEA;--pale:#C7EBF8;--mist:#E9F6FB;
  --backdrop:#7b7b7b;--ink:#3a3a3a;--muted:#8b8b8b;--panel:#f1f2f4;--card-grey:#8d9095;
  --btn-grey:#8e9196;--dark:#1e1e20;--white:#fff;
}
html,body{margin:0;width:1200px;height:777px;overflow:hidden;background:var(--backdrop)}
.stage{position:absolute;left:0;top:0;width:2380px;height:1540px;transform:scale(.5042);transform-origin:0 0}
.page{position:absolute;top:80px;width:386px;height:1380px;background:var(--white);overflow:hidden;font-family:'Open Sans',sans-serif;color:var(--ink)}
.page div,.page span,.page p,.page h2,.page h3,.page a,.page svg,.page i{position:absolute;margin:0}
.head{font-family:'Rajdhani',sans-serif;font-weight:600}

/* top bar + nav */
.topbar{left:196px;top:0;width:190px;height:9px;background:var(--blue);font-size:3px;color:#fff;line-height:9px;white-space:nowrap}
.topbar .tb-phone{left:10px}.topbar .tb-mail{left:40px}
.soc{width:6px;height:6px;border-radius:50%;background:#fff;top:1.5px}
.brand{left:35px;top:12px;height:16px;font-size:5px;color:#8a8a8a;line-height:16px;white-space:nowrap}
.brand i{left:0;top:3px;width:10px;height:10px;border-radius:50%;background:var(--pale)}
.brand span{left:14px}
.nav{top:21px;font-size:3.6px;color:#555;white-space:nowrap}
.nav.active{color:var(--blue)}
.cta{left:310px;top:18px;width:39px;height:12px;background:var(--btn-grey);color:#fff;font-size:3.2px;text-align:center;line-height:12px;font-weight:600}

/* hero */
.hero{left:0;top:40px;width:386px;height:245px}
.hero-1{background:
  radial-gradient(ellipse 28% 22% at 80% 28%,rgba(130,205,255,.75),rgba(130,205,255,0) 70%),
  radial-gradient(ellipse 22% 18% at 22% 18%,rgba(255,130,95,.5),rgba(255,130,95,0) 70%),
  radial-gradient(ellipse 35% 25% at 62% 72%,rgba(70,120,255,.7),rgba(70,120,255,0) 70%),
  radial-gradient(ellipse 20% 15% at 12% 82%,rgba(255,90,140,.45),rgba(255,90,140,0) 70%),
  linear-gradient(135deg,#081647 0%,#1a3cb0 40%,#2a1f7a 65%,#0a1030)}
.hero-2{background:
  radial-gradient(ellipse 30% 30% at 32% 30%,rgba(255,255,255,.85),rgba(255,255,255,0) 70%),
  radial-gradient(ellipse 50% 20% at 70% 70%,rgba(160,200,80,.7),rgba(160,200,80,0) 70%),
  linear-gradient(180deg,#a9cbe8 0%,#dce9f2 32%,#c9dbe4 44%,#8db552 54%,#5c9632 68%,#2f5e20 84%,#22451a)}
.hero-3{background:
  radial-gradient(ellipse 30% 20% at 60% 30%,rgba(255,255,255,.8),rgba(255,255,255,0) 70%),
  linear-gradient(180deg,#8fc1ea 0%,#d3e7f6 30%,#a9c3d9 42%,#6d8fb4 52%,#2e5f9c 62%,#1c3f78 78%,#13284f)}
.hero-4{background:
  radial-gradient(ellipse 26% 22% at 52% 26%,#f6fbe9 0%,rgba(246,251,233,0) 100%),
  radial-gradient(ellipse 30% 40% at 20% 60%,rgba(40,90,25,.8),rgba(40,90,25,0) 70%),
  radial-gradient(ellipse 30% 40% at 85% 65%,rgba(35,80,22,.8),rgba(35,80,22,0) 70%),
  radial-gradient(circle at 50% 30%,#cfe89a 0%,#8cc34c 28%,#4d8a2a 58%,#2a5a1c)}
.hero-5{background:
  radial-gradient(ellipse 35% 18% at 30% 60%,#fff,rgba(255,255,255,0) 80%),
  radial-gradient(ellipse 35% 18% at 75% 52%,#fbfdff,rgba(255,255,255,0) 80%),
  linear-gradient(180deg,#4f97d8 0%,#9fc8ee 26%,#e4eef8 48%,#f5f8fb 65%,#d8e3ee)}
.hero-title{left:35px;top:127px;padding:0 6px;height:21px;line-height:22px;background:rgba(0,148,212,.88);color:#fff;font-size:14px;white-space:nowrap}
.hero-sub{left:35px;top:152px;padding:0 6px;height:20px;line-height:21px;background:rgba(100,104,110,.82);color:#fff;font-size:11px;font-weight:500;white-space:nowrap}
.dot{top:249px;width:3px;height:3px;border-radius:50%;background:#fff}
.hero-curve{left:0;top:225px;width:386px;height:65px}

/* welcome */
.eyebrow{left:36px;top:294px;font-size:8px;color:#444;font-weight:500}
.welcome-title{left:36px;top:305px;font-size:11.5px;color:var(--blue)}
.body-copy{font-size:3.3px;line-height:1.8;color:#7d7d7d;text-align:justify}
.welcome-copy{left:36px;top:327px;width:163px}
.btn-solid{height:16px;line-height:16px;background:var(--blue);color:#fff;font-size:3.4px;font-weight:700;text-align:center}
.welcome-btn{left:36px;top:391px;width:48px}
.ribbon{left:222px;top:295px;width:92px;height:130px;border-radius:45% 55% 40% 60%;background:radial-gradient(ellipse at 40% 35%,var(--sky),rgba(111,204,234,.4) 45%,rgba(199,235,248,.25) 65%,rgba(255,255,255,0))}

/* services */
.services{left:0;top:438px;width:386px;height:205px;background:var(--panel)}
.section-title{left:0;width:386px;text-align:center;font-size:13px;color:#444;font-weight:500}
.section-title b{color:var(--blue);font-weight:600}
.svc-title{top:14px}
.faint{width:40px;height:50px;border-radius:50%;background:radial-gradient(ellipse,rgba(111,204,234,.35),rgba(241,242,244,0) 70%)}
.card{top:39px;width:74px;height:143px;border-radius:2px;overflow:hidden;color:#fff;text-align:center}
.card.blue{background:#1d8fd6}.card.grey{background:var(--card-grey)}
.card-img{left:0;top:0;width:74px;height:67px}
.img-dash{background:radial-gradient(ellipse 40% 30% at 60% 40%,rgba(120,230,255,.8),rgba(120,230,255,0) 70%),linear-gradient(160deg,#0d2a55,#1b6fb8 50%,#7ccff0)}
.img-laptop{background:radial-gradient(ellipse 40% 25% at 50% 75%,rgba(230,120,90,.6),rgba(230,120,90,0) 70%),linear-gradient(160deg,#12204a,#2d4f9a 50%,#6f86b8)}
.img-city{background:radial-gradient(ellipse 45% 30% at 50% 70%,rgba(255,170,80,.45),rgba(255,170,80,0) 70%),linear-gradient(180deg,#0a2a55,#1a5a9a 55%,#0c2240)}
.img-tablet{background:radial-gradient(ellipse 40% 35% at 55% 55%,rgba(255,255,255,.8),rgba(255,255,255,0) 70%),linear-gradient(160deg,#1e5fa8,#6fb2e4 50%,#d9ebf7)}
.card-name{left:4px;top:75px;width:66px;font-size:3.6px;font-weight:700;line-height:1.5}
.card-copy{left:5px;top:94px;width:64px;font-size:2.9px;line-height:1.6;opacity:.9}
.card-btn{left:23px;top:123px;width:28px;height:9px;line-height:9px;border:.6px solid #fff;font-size:2.9px}
.arrow{top:103px;width:11px;height:11px;border-radius:50%;background:#fff;border:.6px solid #bbb}

/* publications */
.pub-title{top:657px}
.underline{left:183px;top:674px;width:20px;height:1px;background:var(--blue)}
.pub-img{width:157px;height:98px;background:
  radial-gradient(ellipse 30% 25% at 35% 55%,rgba(255,160,60,.85),rgba(255,160,60,0) 70%),
  radial-gradient(ellipse 25% 20% at 70% 40%,rgba(255,200,110,.7),rgba(255,200,110,0) 70%),
  radial-gradient(ellipse 40% 30% at 60% 80%,rgba(60,170,230,.6),rgba(60,170,230,0) 70%),
  linear-gradient(160deg,#0c1d36,#183f6a 50%,#0f2542)}
.pub-img.chart{background:
  radial-gradient(ellipse 30% 25% at 45% 55%,rgba(80,230,180,.6),rgba(80,230,180,0) 70%),
  radial-gradient(ellipse 25% 30% at 85% 25%,rgba(230,200,170,.6),rgba(230,200,170,0) 70%),
  linear-gradient(135deg,#0a1b30,#1b5183 45%,#36a6c6 68%,#0c2038)}
.pub-head{font-size:4.7px;color:var(--blue);font-weight:600;line-height:1.55;width:130px}
.pub-copy{width:133px}
.btn-outline{width:42px;height:13px;line-height:13px;border:.7px solid var(--blue);color:var(--blue);font-size:3.2px;font-weight:600;text-align:center}

/* team */
.team-title{top:928px}
.member{top:960px;width:65px;height:100px;background:#fff;box-shadow:0 0 3px rgba(0,0,0,.15);text-align:center}
.avatar{left:15px;top:-3px;width:34px;height:34px;border-radius:50%;border:1.5px solid #fff;box-shadow:0 0 2px rgba(0,0,0,.25);background:linear-gradient(180deg,#e6e8eb 0%,#d3c3b4 40%,#b89a84 55%,#3d4047 72%,#25272c)}
.avatar.warm{background:linear-gradient(180deg,#e6e8eb 0%,#caa58a 40%,#8d6a52 55%,#2e2f35 72%,#1d1e22)}
.avatar.dark{background:linear-gradient(180deg,#e9eaec 0%,#4b3a30 35%,#c59c82 55%,#25262b 75%,#18191c)}
.member-name{left:0;top:36px;width:65px;font-size:3.5px;color:var(--blue);font-weight:700}
.member-role{left:0;top:43px;width:65px;font-size:2.8px;color:#888}
.member-bio{left:5px;top:52px;width:55px;font-size:2.8px;line-height:1.6;color:#888}
.member-link{left:27px;top:94px;width:10px;height:10px;border-radius:50%;background:var(--blue)}

/* about */
.about{left:0;top:1090px;width:386px;height:170px;background:#f4f5f6}
.about-img{left:0;top:1090px;width:205px;height:165px;background:
  radial-gradient(ellipse 32% 20% at 35% 30%,rgba(40,70,110,.95),rgba(30,45,70,.9) 60%,rgba(30,45,70,0) 75%),
  radial-gradient(ellipse 18% 12% at 72% 48%,rgba(40,60,90,.85),rgba(40,60,90,0) 75%),
  linear-gradient(90deg,#d9dde2 0%,#eef0f2 40%,#f6f7f8 70%,#f4f5f6),
  linear-gradient(180deg,#eceef1 0%,#f4f5f6 60%,#e2e5e9)}
.about-title{left:225px;top:1106px;font-size:13px;color:#444;font-weight:500}
.about-copy{left:225px;top:1128px;width:115px}
.about-btn{left:225px;top:1214px;width:47px;height:16px;line-height:16px;background:var(--btn-grey);color:#fff;font-size:3.3px;text-align:center;font-weight:600}

/* footer */
.foot-shape{left:0;top:1232px;width:386px;height:148px}
.foot-brand{left:0;top:1273px;width:386px;height:14px;font-size:8px;color:#9a9a9a;white-space:nowrap}
.foot-brand i{left:134px;top:2px;width:9px;height:9px;border-radius:50%;border:.7px solid #9a9a9a}
.foot-brand span{left:147px;top:0}
.foot-nav{top:1304px;font-size:3.2px;color:#ddd;font-weight:700;white-space:nowrap}
.foot-ico{top:1329px;width:11px;height:11px;border-radius:50%;border:.7px solid #ddd}
.foot-ico svg{left:2.5px;top:2.5px;width:6px;height:6px}
.foot-text{top:1330px;font-size:3px;line-height:1.6;color:#ddd;white-space:nowrap}
.foot-soc{top:1361px;width:10px;height:10px;border-radius:50%;border:.7px solid #ddd}
.copyright{left:245px;top:1364px;font-size:3px;color:#ddd;white-space:nowrap}
</style>
</head>
<body>
<div class="stage">

<!-- PAGE 1 -->
<div class="page" style="left:88px">
  <div class="topbar"><span class="tb-phone">☎ 404.555.0187</span><span class="tb-mail">✉ info@tidewellmetrics.com</span><i class="soc" style="left:160px"></i><i class="soc" style="left:168px"></i><i class="soc" style="left:176px"></i></div>
  <div class="brand"><i></i><span>Tidewell Metrics Group</span></div>
  <a class="nav active" style="left:133px">Home</a><a class="nav" style="left:156px">Core Services</a><a class="nav" style="left:197px">About Us</a><a class="nav" style="left:228px">Our Work</a><a class="nav" style="left:259px">Blog</a><a class="nav" style="left:279px">Contact Us</a>
  <div class="cta">GET STARTED</div>
  <div class="hero hero-1" role="img" aria-label="Hand touching a glowing financial analytics screen"></div>
  <div class="hero-title head">Tidewell Metrics Group</div>
  <div class="hero-sub head">Data Driven Research &amp; Insights</div>
  <i class="dot" style="left:186px"></i><i class="dot" style="left:192px;opacity:.6"></i>
  <svg class="hero-curve" viewBox="0 0 386 65"><path d="M0 55C130 60 260 42 386 14V65H0Z" fill="#fff"/><path d="M160 54C250 48 330 34 386 12" fill="none" stroke="#0094D4" stroke-width="4"/></svg>
  <p class="eyebrow head">Welcome To</p>
  <h2 class="welcome-title head">Tidewell Metrics Group</h2>
  <p class="welcome-copy body-copy">Tidewell Metrics Group was formed in 2016 to help utilities and regulatory agencies navigate the technical, economic, and policy challenges of building a smarter and cleaner energy future. Through cutting edge research design and analysis methods we provide DSM program administrators with data-driven insights into how various technologies and interventions affect the way homes and businesses use energy.</p>
  <div class="welcome-btn btn-solid">READ MORE</div>
  <div class="ribbon" role="img" aria-label="Dotted blue ribbon graphic"></div>
  <div class="services">
    <i class="faint" style="left:2px;top:8px"></i><i class="faint" style="left:344px;top:135px"></i>
    <h2 class="section-title svc-title head">Our <b>Services</b></h2>
    <i class="arrow" style="left:14px"></i><i class="arrow" style="left:361px"></i>
    <div class="card blue" style="left:36px"><div class="card-img img-dash" role="img" aria-label="Analytics dashboard on a laptop"></div><span class="card-name">Predictive Analytics and Forecasting</span><span class="card-copy">Distributed energy resource integration into planning and operations</span><span class="card-btn">Read More</span></div>
    <div class="card grey" style="left:116px"><div class="card-img img-laptop" role="img" aria-label="Laptop showing data charts"></div><span class="card-name">T&amp;D Planning</span><span class="card-copy">Location specific, probabilistic forecasting for system-level T&amp;D planning</span><span class="card-btn">Read More</span></div>
    <div class="card blue" style="left:196px"><div class="card-img img-city" role="img" aria-label="City skyline with data overlay"></div><span class="card-name">Pilot &amp; Emerging Tech Support</span><span class="card-copy">Design and implementation of pilots and controlled deployments</span><span class="card-btn">Read More</span></div>
    <div class="card grey" style="left:277px"><div class="card-img img-tablet" role="img" aria-label="Tablet with analytics graphs"></div><span class="card-name">Program Portfolio &amp; Resource Planning</span><span class="card-copy">End-use load profile studies &amp; research baseline studies</span><span class="card-btn">Read More</span></div>
  </div>
  <h2 class="section-title pub-title head">Publications</h2><i class="underline"></i>
  <div class="pub-img" style="left:36px;top:686px" role="img" aria-label="Night city lights from above"></div>
  <h3 class="pub-head" style="left:209px;top:693px">Journal Articles and Conference Presentations</h3>
  <p class="pub-copy body-copy" style="left:209px;top:717px">Sed ut perspiciatis unde omnis iste natus error sit voluptatem accusantium doloremque laudantium, totam rem aperiam, eaque ipsa quae ab illo inventore veritatis et quasi architecto beatae vitae dicta sunt explicabo.</p>
  <div class="btn-outline" style="left:209px;top:760px">READ MORE</div>
  <h3 class="pub-head" style="left:47px;top:805px">Published Reports</h3>
  <p class="pub-copy body-copy" style="left:47px;top:819px">Sed ut perspiciatis unde omnis iste natus error sit voluptatem accusantium doloremque laudantium, totam rem aperiam, eaque ipsa quae ab illo inventore veritatis et quasi architecto beatae vitae dicta sunt explicabo.</p>
  <div class="btn-outline" style="left:47px;top:861px">READ MORE</div>
  <div class="pub-img chart" style="left:193px;top:785px" role="img" aria-label="Hand pointing at stock charts on a screen"></div>
  <h2 class="section-title team-title head">Our <b>Teams</b></h2>
  <div class="member" style="left:36px"><div class="avatar" role="img" aria-label="Portrait photo of team member"></div><span class="member-name">Marcus Hale, M.S.</span><span class="member-role">Partner</span><span class="member-bio">Marcus is an applied statistician whose work centers on estimating demand impacts.</span><i class="member-link"></i></div>
  <div class="member" style="left:118px"><div class="avatar warm" role="img" aria-label="Portrait photo of team member"></div><span class="member-name">Owen Prater, M.P.P.</span><span class="member-role">Partner</span><span class="member-bio">Owen specializes in novel applications of data analytics using large volumes of hourly data.</span><i class="member-link"></i></div>
  <div class="member" style="left:201px"><div class="avatar dark" role="img" aria-label="Portrait photo of team member"></div><span class="member-name">Lena Varga</span><span class="member-role">Partner</span><span class="member-bio">Lena's work has focused on distributed energy resources and solar photovoltaic systems.</span><i class="member-link"></i></div>
  <div class="member" style="left:283px"><div class="avatar dark" role="img" aria-label="Portrait photo of team member"></div><span class="member-name">Selma Ortiz, M.S.</span><span class="member-role">Partner</span><span class="member-bio">Selma has extensive expertise with analysis of smart meter data.</span><i class="member-link"></i></div>
  <div class="about"></div>
  <div class="about-img" role="img" aria-label="Desk with computer monitors showing analytics"></div>
  <h2 class="about-title head">About Us</h2>
  <p class="about-copy body-copy">Tidewell Metrics Group (TMG) was formed in 2016 to help utilities and regulatory agencies navigate the technical, economic, and policy challenges of building a smarter and cleaner energy future. Our research focuses on impact analysis as well as predictive &amp; causal analytics. We deliver data-driven insights into how various technologies and interventions affect the way homes and businesses use energy and how those in turn affect grid and system planning.</p>
  <div class="about-btn">READ MORE</div>
  <svg class="foot-shape" viewBox="0 0 386 148"><path d="M0 20C130 10 270 14 386 52V148H0Z" fill="#1e1e20"/><path d="M140 13C250 16 330 32 386 50" fill="none" stroke="#0094D4" stroke-width="3"/></svg>
  <div class="foot-brand"><i></i><span>Tidewell Metrics Group</span></div>
  <a class="foot-nav" style="left:91px">HOME</a><a class="foot-nav" style="left:118px">CORE SERVICES</a><a class="foot-nav" style="left:167px">ABOUT US</a><a class="foot-nav" style="left:203px">OUR WORK</a><a class="foot-nav" style="left:242px">BLOG</a><a class="foot-nav" style="left:267px">CONTACT US</a>
  <i class="foot-ico" style="left:36px"><svg viewBox="0 0 6 6"><path d="M3 6C1 3.6 1 2.6 1 2a2 2 0 0 1 4 0c0 .6 0 1.6-2 4Z" fill="#ddd"/></svg></i>
  <span class="foot-text" style="left:51px">120 Harbor Line Rd NE<br>Suite 4 Atlanta, GA 30301</span>
  <i class="foot-ico" style="left:177px"><svg viewBox="0 0 6 6"><path d="M1 .5h1.3l.6 1.4-.8.6a3.5 3.5 0 0 0 1.4 1.4l.6-.8 1.4.6V5c-2.6.3-4.8-1.9-4.5-4.5Z" fill="#ddd"/></svg></i>
  <span class="foot-text" style="left:193px;top:1333px">404.555.0187</span>
  <i class="foot-ico" style="left:258px"><svg viewBox="0 0 6 6"><rect x=".5" y="1.2" width="5" height="3.6" fill="none" stroke="#ddd" stroke-width=".6"/><path d="M.5 1.2 3 3.2 5.5 1.2" fill="none" stroke="#ddd" stroke-width=".6"/></svg></i>
  <span class="foot-text" style="left:275px;top:1333px">info@tidewellmetrics.com</span>
  <i class="foot-soc" style="left:36px"></i><i class="foot-soc" style="left:51px"></i><i class="foot-soc" style="left:66px"></i>
  <span class="copyright">© 2022 Tidewell Metrics Group. All rights reserved</span>
</div>

<!-- PAGE 2 -->
<div class="page" style="left:538px">
  <div class="topbar"><span class="tb-phone">☎ 404.555.0187</span><span class="tb-mail">✉ info@tidewellmetrics.com</span><i class="soc" style="left:160px"></i><i class="soc" style="left:168px"></i><i class="soc" style="left:176px"></i></div>
  <div class="brand"><i></i><span>Tidewell Metrics Group</span></div>
  <a class="nav active" style="left:133px">Home</a><a class="nav" style="left:156px">Core Services</a><a class="nav" style="left:197px">About Us</a><a class="nav" style="left:228px">Our Work</a><a class="nav" style="left:259px">Blog</a><a class="nav" style="left:279px">Contact Us</a>
  <div class="cta">GET STARTED</div>
  <div class="hero hero-2" role="img" aria-label="Wind turbines over green fields and forest"></div>
  <div class="hero-title head">Tidewell Metrics Group</div>
  <div class="hero-sub head">Data Driven Research &amp; Insights</div>
  <i class="dot" style="left:186px;opacity:.6"></i><i class="dot" style="left:192px"></i><i class="dot" style="left:198px;opacity:.6"></i>
  <svg class="hero-curve" viewBox="0 0 386 65"><path d="M0 55C130 60 260 42 386 14V65H0Z" fill="#fff"/><path d="M160 54C250 48 330 34 386 12" fill="none" stroke="#0094D4" stroke-width="4"/></svg>
  <p class="eyebrow head">Welcome To</p>
  <h2 class="welcome-title head">Tidewell Metrics Group</h2>
  <p class="welcome-copy body-copy">Tidewell Metrics Group was formed in 2016 to help utilities and regulatory agencies navigate the technical, economic, and policy challenges of building a smarter and cleaner energy future. Through cutting edge research design and analysis methods we provide DSM program administrators with data-driven insights into how various technologies and interventions affect the way homes and businesses use energy.</p>
  <div class="welcome-btn btn-solid">READ MORE</div>
  <div class="ribbon" role="img" aria-label="Dotted blue ribbon graphic"></div>
  <div class="services">
    <i class="faint" style="left:2px;top:8px"></i><i class="faint" style="left:344px;top:135px"></i>
    <h2 class="section-title svc-title head">Our <b>Services</b></h2>
    <i class="arrow" style="left:14px"></i><i class="arrow" style="left:361px"></i>
    <div class="card blue" style="left:36px"><div class="card-img img-dash" role="img" aria-label="Analytics dashboard on a laptop"></div><span class="card-name">Predictive Analytics and Forecasting</span><span class="card-copy">Distributed energy resource integration into planning and operations</span><span class="card-btn">Read More</span></div>
    <div class="card grey" style="left:116px"><div class="card-img img-laptop" role="img" aria-label="Laptop showing data charts"></div><span class="card-name">T&amp;D Planning</span><span class="card-copy">Location specific, probabilistic forecasting for system-level T&amp;D planning</span><span class="card-btn">Read More</span></div>
    <div class="card blue" style="left:196px"><div class="card-img img-city" role="img" aria-label="City skyline with data overlay"></div><span class="card-name">Pilot &amp; Emerging Tech Support</span><span class="card-copy">Design and implementation of pilots and controlled deployments</span><span class="card-btn">Read More</span></div>
    <div class="card grey" style="left:277px"><div class="card-img img-tablet" role="img" aria-label="Tablet with analytics graphs"></div><span class="card-name">Program Portfolio &amp; Resource Planning</span><span class="card-copy">End-use load profile studies &amp; research baseline studies</span><span class="card-btn">Read More</span></div>
  </div>
  <h2 class="section-title pub-title head">Publications</h2><i class="underline"></i>
  <div class="pub-img" style="left:36px;top:686px" role="img" aria-label="Night city lights from above"></div>
  <h3 class="pub-head" style="left:209px;top:693px">Journal Articles and Conference Presentations</h3>
  <p class="pub-copy body-copy" style="left:209px;top:717px">Sed ut perspiciatis unde omnis iste natus error sit voluptatem accusantium doloremque laudantium, totam rem aperiam, eaque ipsa quae ab illo inventore veritatis et quasi architecto beatae vitae dicta sunt explicabo.</p>
  <div class="btn-outline" style="left:209px;top:760px">READ MORE</div>
  <h3 class="pub-head" style="left:47px;top:805px">Published Reports</h3>
  <p class="pub-copy body-copy" style="left:47px;top:819px">Sed ut perspiciatis unde omnis iste natus error sit voluptatem accusantium doloremque laudantium, totam rem aperiam, eaque ipsa quae ab illo inventore veritatis et quasi architecto beatae vitae dicta sunt explicabo.</p>
  <div class="btn-outline" style="left:47px;top:861px">READ MORE</div>
  <div class="pub-img chart" style="left:193px;top:785px" role="img" aria-label="Hand pointing at stock charts on a screen"></div>
  <h2 class="section-title team-title head">Our <b>Teams</b></h2>
  <div class="member" style="left:36px"><div class="avatar" role="img" aria-label="Portrait photo of team member"></div><span class="member-name">Marcus Hale, M.S.</span><span class="member-role">Partner</span><span class="member-bio">Marcus is an applied statistician whose work centers on estimating demand impacts.</span><i class="member-link"></i></div>
  <div class="member" style="left:118px"><div class="avatar warm" role="img" aria-label="Portrait photo of team member"></div><span class="member-name">Owen Prater, M.P.P.</span><span class="member-role">Partner</span><span class="member-bio">Owen specializes in novel applications of data analytics using large volumes of hourly data.</span><i class="member-link"></i></div>
  <div class="member" style="left:201px"><div class="avatar dark" role="img" aria-label="Portrait photo of team member"></div><span class="member-name">Lena Varga</span><span class="member-role">Partner</span><span class="member-bio">Lena's work has focused on distributed energy resources and solar photovoltaic systems.</span><i class="member-link"></i></div>
  <div class="member" style="left:283px"><div class="avatar dark" role="img" aria-label="Portrait photo of team member"></div><span class="member-name">Selma Ortiz, M.S.</span><span class="member-role">Partner</span><span class="member-bio">Selma has extensive expertise with analysis of smart meter data.</span><i class="member-link"></i></div>
  <div class="about"></div>
  <div class="about-img" role="img" aria-label="Desk with computer monitors showing analytics"></div>
  <h2 class="about-title head">About Us</h2>
  <p class="about-copy body-copy">Tidewell Metrics Group (TMG) was formed in 2016 to help utilities and regulatory agencies navigate the technical, economic, and policy challenges of building a smarter and cleaner energy future. Our research focuses on impact analysis as well as predictive &amp; causal analytics. We deliver data-driven insights into how various technologies and interventions affect the way homes and businesses use energy and how those in turn affect grid and system planning.</p>
  <div class="about-btn">READ MORE</div>
  <svg class="foot-shape" viewBox="0 0 386 148"><path d="M0 20C130 10 270 14 386 52V148H0Z" fill="#1e1e20"/><path d="M140 13C250 16 330 32 386 50" fill="none" stroke="#0094D4" stroke-width="3"/></svg>
  <div class="foot-brand"><i></i><span>Tidewell Metrics Group</span></div>
  <a class="foot-nav" style="left:91px">HOME</a><a class="foot-nav" style="left:118px">CORE SERVICES</a><a class="foot-nav" style="left:167px">ABOUT US</a><a class="foot-nav" style="left:203px">OUR WORK</a><a class="foot-nav" style="left:242px">BLOG</a><a class="foot-nav" style="left:267px">CONTACT US</a>
  <i class="foot-ico" style="left:36px"><svg viewBox="0 0 6 6"><path d="M3 6C1 3.6 1 2.6 1 2a2 2 0 0 1 4 0c0 .6 0 1.6-2 4Z" fill="#ddd"/></svg></i>
  <span class="foot-text" style="left:51px">120 Harbor Line Rd NE<br>Suite 4 Atlanta, GA 30301</span>
  <i class="foot-ico" style="left:177px"><svg viewBox="0 0 6 6"><path d="M1 .5h1.3l.6 1.4-.8.6a3.5 3.5 0 0 0 1.4 1.4l.6-.8 1.4.6V5c-2.6.3-4.8-1.9-4.5-4.5Z" fill="#ddd"/></svg></i>
  <span class="foot-text" style="left:193px;top:1333px">404.555.0187</span>
  <i class="foot-ico" style="left:258px"><svg viewBox="0 0 6 6"><rect x=".5" y="1.2" width="5" height="3.6" fill="none" stroke="#ddd" stroke-width=".6"/><path d="M.5 1.2 3 3.2 5.5 1.2" fill="none" stroke="#ddd" stroke-width=".6"/></svg></i>
  <span class="foot-text" style="left:275px;top:1333px">info@tidewellmetrics.com</span>
  <i class="foot-soc" style="left:36px"></i><i class="foot-soc" style="left:51px"></i><i class="foot-soc" style="left:66px"></i>
  <span class="copyright">© 2022 Tidewell Metrics Group. All rights reserved</span>
</div>

<!-- PAGE 3 -->
<div class="page" style="left:989px">
  <div class="topbar"><span class="tb-phone">☎ 404.555.0187</span><span class="tb-mail">✉ info@tidewellmetrics.com</span><i class="soc" style="left:160px"></i><i class="soc" style="left:168px"></i><i class="soc" style="left:176px"></i></div>
  <div class="brand"><i></i><span>Tidewell Metrics Group</span></div>
  <a class="nav active" style="left:133px">Home</a><a class="nav" style="left:156px">Core Services</a><a class="nav" style="left:197px">About Us</a><a class="nav" style="left:228px">Our Work</a><a class="nav" style="left:259px">Blog</a><a class="nav" style="left:279px">Contact Us</a>
  <div class="cta">GET STARTED</div>
  <div class="hero hero-3" role="img" aria-label="Wind turbines and solar panels under mountains"></div>
  <div class="hero-title head">Tidewell Metrics Group</div>
  <div class="hero-sub head">Data Driven Research &amp; Insights</div>
  <i class="dot" style="left:186px"></i><i class="dot" style="left:196px;opacity:.6"></i>
  <svg class="hero-curve" viewBox="0 0 386 65"><path d="M0 55C130 60 260 42 386 14V65H0Z" fill="#fff"/><path d="M160 54C250 48 330 34 386 12" fill="none" stroke="#0094D4" stroke-width="4"/></svg>
  <p class="eyebrow head">Welcome To</p>
  <h2 class="welcome-title head">Tidewell Metrics Group</h2>
  <p class="welcome-copy body-copy">Tidewell Metrics Group was formed in 2016 to help utilities and regulatory agencies navigate the technical, economic, and policy challenges of building a smarter and cleaner energy future. Through cutting edge research design and analysis methods we provide DSM program administrators with data-driven insights into how various technologies and interventions affect the way homes and businesses use energy.</p>
  <div class="welcome-btn btn-solid">READ MORE</div>
  <div class="ribbon" role="img" aria-label="Dotted blue ribbon graphic"></div>
  <div class="services">
    <i class="faint" style="left:2px;top:8px"></i><i class="faint" style="left:344px;top:135px"></i>
    <h2 class="section-title svc-title head">Our <b>Services</b></h2>
    <i class="arrow" style="left:14px"></i><i class="arrow" style="left:361px"></i>
    <div class="card blue" style="left:36px"><div class="card-img img-dash" role="img" aria-label="Analytics dashboard on a laptop"></div><span class="card-name">Predictive Analytics and Forecasting</span><span class="card-copy">Distributed energy resource integration into planning and operations</span><span class="card-btn">Read More</span></div>
    <div class="card grey" style="left:116px"><div class="card-img img-laptop" role="img" aria-label="Laptop showing data charts"></div><span class="card-name">T&amp;D Planning</span><span class="card-copy">Location specific, probabilistic forecasting for system-level T&amp;D planning</span><span class="card-btn">Read More</span></div>
    <div class="card blue" style="left:196px"><div class="card-img img-city" role="img" aria-label="City skyline with data overlay"></div><span class="card-name">Pilot &amp; Emerging Tech Support</span><span class="card-copy">Design and implementation of pilots and controlled deployments</span><span class="card-btn">Read More</span></div>
    <div class="card grey" style="left:277px"><div class="card-img img-tablet" role="img" aria-label="Tablet with analytics graphs"></div><span class="card-name">Program Portfolio &amp; Resource Planning</span><span class="card-copy">End-use load profile studies &amp; research baseline studies</span><span class="card-btn">Read More</span></div>
  </div>
  <h2 class="section-title pub-title head">Publications</h2><i class="underline"></i>
  <div class="pub-img" style="left:36px;top:686px" role="img" aria-label="Night city lights from above"></div>
  <h3 class="pub-head" style="left:209px;top:693px">Journal Articles and Conference Presentations</h3>
  <p class="pub-copy body-copy" style="left:209px;top:717px">Sed ut perspiciatis unde omnis iste natus error sit voluptatem accusantium doloremque laudantium, totam rem aperiam, eaque ipsa quae ab illo inventore veritatis et quasi architecto beatae vitae dicta sunt explicabo.</p>
  <div class="btn-outline" style="left:209px;top:760px">READ MORE</div>
  <h3 class="pub-head" style="left:47px;top:805px">Published Reports</h3>
  <p class="pub-copy body-copy" style="left:47px;top:819px">Sed ut perspiciatis unde omnis iste natus error sit voluptatem accusantium doloremque laudantium, totam rem aperiam, eaque ipsa quae ab illo inventore veritatis et quasi architecto beatae vitae dicta sunt explicabo.</p>
  <div class="btn-outline" style="left:47px;top:861px">READ MORE</div>
  <div class="pub-img chart" style="left:193px;top:785px" role="img" aria-label="Hand pointing at stock charts on a screen"></div>
  <h2 class="section-title team-title head">Our <b>Teams</b></h2>
  <div class="member" style="left:36px"><div class="avatar" role="img" aria-label="Portrait photo of team member"></div><span class="member-name">Marcus Hale, M.S.</span><span class="member-role">Partner</span><span class="member-bio">Marcus is an applied statistician whose work centers on estimating demand impacts.</span><i class="member-link"></i></div>
  <div class="member" style="left:118px"><div class="avatar warm" role="img" aria-label="Portrait photo of team member"></div><span class="member-name">Owen Prater, M.P.P.</span><span class="member-role">Partner</span><span class="member-bio">Owen specializes in novel applications of data analytics using large volumes of hourly data.</span><i class="member-link"></i></div>
  <div class="member" style="left:201px"><div class="avatar dark" role="img" aria-label="Portrait photo of team member"></div><span class="member-name">Lena Varga</span><span class="member-role">Partner</span><span class="member-bio">Lena's work has focused on distributed energy resources and solar photovoltaic systems.</span><i class="member-link"></i></div>
  <div class="member" style="left:283px"><div class="avatar dark" role="img" aria-label="Portrait photo of team member"></div><span class="member-name">Selma Ortiz, M.S.</span><span class="member-role">Partner</span><span class="member-bio">Selma has extensive expertise with analysis of smart meter data.</span><i class="member-link"></i></div>
  <div class="about"></div>
  <div class="about-img" role="img" aria-label="Desk with computer monitors showing analytics"></div>
  <h2 class="about-title head">About Us</h2>
  <p class="about-copy body-copy">Tidewell Metrics Group (TMG) was formed in 2016 to help utilities and regulatory agencies navigate the technical, economic, and policy challenges of building a smarter and cleaner energy future. Our research focuses on impact analysis as well as predictive &amp; causal analytics. We deliver data-driven insights into how various technologies and interventions affect the way homes and businesses use energy and how those in turn affect grid and system planning.</p>
  <div class="about-btn">READ MORE</div>
  <svg class="foot-shape" viewBox="0 0 386 148"><path d="M0 20C130 10 270 14 386 52V148H0Z" fill="#1e1e20"/><path d="M140 13C250 16 330 32 386 50" fill="none" stroke="#0094D4" stroke-width="3"/></svg>
  <div class="foot-brand"><i></i><span>Tidewell Metrics Group</span></div>
  <a class="foot-nav" style="left:91px">HOME</a><a class="foot-nav" style="left:118px">CORE SERVICES</a><a class="foot-nav" style="left:167px">ABOUT US</a><a class="foot-nav" style="left:203px">OUR WORK</a><a class="foot-nav" style="left:242px">BLOG</a><a class="foot-nav" style="left:267px">CONTACT US</a>
  <i class="foot-ico" style="left:36px"><svg viewBox="0 0 6 6"><path d="M3 6C1 3.6 1 2.6 1 2a2 2 0 0 1 4 0c0 .6 0 1.6-2 4Z" fill="#ddd"/></svg></i>
  <span class="foot-text" style="left:51px">120 Harbor Line Rd NE<br>Suite 4 Atlanta, GA 30301</span>
  <i class="foot-ico" style="left:177px"><svg viewBox="0 0 6 6"><path d="M1 .5h1.3l.6 1.4-.8.6a3.5 3.5 0 0 0 1.4 1.4l.6-.8 1.4.6V5c-2.6.3-4.8-1.9-4.5-4.5Z" fill="#ddd"/></svg></i>
  <span class="foot-text" style="left:193px;top:1333px">404.555.0187</span>
  <i class="foot-ico" style="left:258px"><svg viewBox="0 0 6 6"><rect x=".5" y="1.2" width="5" height="3.6" fill="none" stroke="#ddd" stroke-width=".6"/><path d="M.5 1.2 3 3.2 5.5 1.2" fill="none" stroke="#ddd" stroke-width=".6"/></svg></i>
  <span class="foot-text" style="left:275px;top:1333px">info@tidewellmetrics.com</span>
  <i class="foot-soc" style="left:36px"></i><i class="foot-soc" style="left:51px"></i><i class="foot-soc" style="left:66px"></i>
  <span class="copyright">© 2022 Tidewell Metrics Group. All rights reserved</span>
</div>

<!-- PAGE 4 -->
<div class="page" style="left:1443px">
  <div class="topbar"><span class="tb-phone">☎ 404.555.0187</span><span class="tb-mail">✉ info@tidewellmetrics.com</span><i class="soc" style="left:160px"></i><i class="soc" style="left:168px"></i><i class="soc" style="left:176px"></i></div>
  <div class="brand"><i></i><span>Tidewell Metrics Group</span></div>
  <a class="nav active" style="left:133px">Home</a><a class="nav" style="left:156px">Core Services</a><a class="nav" style="left:197px">About Us</a><a class="nav" style="left:228px">Our Work</a><a class="nav" style="left:259px">Blog</a><a class="nav" style="left:279px">Contact Us</a>
  <div class="cta">GET STARTED</div>
  <div class="hero hero-4" role="img" aria-label="Looking up into green tree canopy"></div>
  <div class="hero-title head">Tidewell Metrics Group</div>
  <div class="hero-sub head">Data Driven Research &amp; Insights</div>
  <i class="dot" style="left:190px"></i><i class="dot" style="left:196px;opacity:.6"></i>
  <svg class="hero-curve" viewBox="0 0 386 65"><path d="M0 55C130 60 260 42 386 14V65H0Z" fill="#fff"/><path d="M160 54C250 48 330 34 386 12" fill="none" stroke="#0094D4" stroke-width="4"/></svg>
  <p class="eyebrow head">Welcome To</p>
  <h2 class="welcome-title head">Tidewell Metrics Group</h2>
  <p class="welcome-copy body-copy">Tidewell Metrics Group was formed in 2016 to help utilities and regulatory agencies navigate the technical, economic, and policy challenges of building a smarter and cleaner energy future. Through cutting edge research design and analysis methods we provide DSM program administrators with data-driven insights into how various technologies and interventions affect the way homes and businesses use energy.</p>
  <div class="welcome-btn btn-solid">READ MORE</div>
  <div class="ribbon" role="img" aria-label="Dotted blue ribbon graphic"></div>
  <div class="services">
    <i class="faint" style="left:2px;top:8px"></i><i class="faint" style="left:344px;top:135px"></i>
    <h2 class="section-title svc-title head">Our <b>Services</b></h2>
    <i class="arrow" style="left:14px"></i><i class="arrow" style="left:361px"></i>
    <div class="card blue" style="left:36px"><div class="card-img img-dash" role="img" aria-label="Analytics dashboard on a laptop"></div><span class="card-name">Predictive Analytics and Forecasting</span><span class="card-copy">Distributed energy resource integration into planning and operations</span><span class="card-btn">Read More</span></div>
    <div class="card grey" style="left:116px"><div class="card-img img-laptop" role="img" aria-label="Laptop showing data charts"></div><span class="card-name">T&amp;D Planning</span><span class="card-copy">Location specific, probabilistic forecasting for system-level T&amp;D planning</span><span class="card-btn">Read More</span></div>
    <div class="card blue" style="left:196px"><div class="card-img img-city" role="img" aria-label="City skyline with data overlay"></div><span class="card-name">Pilot &amp; Emerging Tech Support</span><span class="card-copy">Design and implementation of pilots and controlled deployments</span><span class="card-btn">Read More</span></div>
    <div class="card grey" style="left:277px"><div class="card-img img-tablet" role="img" aria-label="Tablet with analytics graphs"></div><span class="card-name">Program Portfolio &amp; Resource Planning</span><span class="card-copy">End-use load profile studies &amp; research baseline studies</span><span class="card-btn">Read More</span></div>
  </div>
  <h2 class="section-title pub-title head">Publications</h2><i class="underline"></i>
  <div class="pub-img" style="left:36px;top:686px" role="img" aria-label="Night city lights from above"></div>
  <h3 class="pub-head" style="left:209px;top:693px">Journal Articles and Conference Presentations</h3>
  <p class="pub-copy body-copy" style="left:209px;top:717px">Sed ut perspiciatis unde omnis iste natus error sit voluptatem accusantium doloremque laudantium, totam rem aperiam, eaque ipsa quae ab illo inventore veritatis et quasi architecto beatae vitae dicta sunt explicabo.</p>
  <div class="btn-outline" style="left:209px;top:760px">READ MORE</div>
  <h3 class="pub-head" style="left:47px;top:805px">Published Reports</h3>
  <p class="pub-copy body-copy" style="left:47px;top:819px">Sed ut perspiciatis unde omnis iste natus error sit voluptatem accusantium doloremque laudantium, totam rem aperiam, eaque ipsa quae ab illo inventore veritatis et quasi architecto beatae vitae dicta sunt explicabo.</p>
  <div class="btn-outline" style="left:47px;top:861px">READ MORE</div>
  <div class="pub-img chart" style="left:193px;top:785px" role="img" aria-label="Hand pointing at stock charts on a screen"></div>
  <h2 class="section-title team-title head">Our <b>Teams</b></h2>
  <div class="member" style="left:36px"><div class="avatar" role="img" aria-label="Portrait photo of team member"></div><span class="member-name">Marcus Hale, M.S.</span><span class="member-role">Partner</span><span class="member-bio">Marcus is an applied statistician whose work centers on estimating demand impacts.</span><i class="member-link"></i></div>
  <div class="member" style="left:118px"><div class="avatar warm" role="img" aria-label="Portrait photo of team member"></div><span class="member-name">Owen Prater, M.P.P.</span><span class="member-role">Partner</span><span class="member-bio">Owen specializes in novel applications of data analytics using large volumes of hourly data.</span><i class="member-link"></i></div>
  <div class="member" style="left:201px"><div class="avatar dark" role="img" aria-label="Portrait photo of team member"></div><span class="member-name">Lena Varga</span><span class="member-role">Partner</span><span class="member-bio">Lena's work has focused on distributed energy resources and solar photovoltaic systems.</span><i class="member-link"></i></div>
  <div class="member" style="left:283px"><div class="avatar dark" role="img" aria-label="Portrait photo of team member"></div><span class="member-name">Selma Ortiz, M.S.</span><span class="member-role">Partner</span><span class="member-bio">Selma has extensive expertise with analysis of smart meter data.</span><i class="member-link"></i></div>
  <div class="about"></div>
  <div class="about-img" role="img" aria-label="Desk with computer monitors showing analytics"></div>
  <h2 class="about-title head">About Us</h2>
  <p class="about-copy body-copy">Tidewell Metrics Group (TMG) was formed in 2016 to help utilities and regulatory agencies navigate the technical, economic, and policy challenges of building a smarter and cleaner energy future. Our research focuses on impact analysis as well as predictive &amp; causal analytics. We deliver data-driven insights into how various technologies and interventions affect the way homes and businesses use energy and how those in turn affect grid and system planning.</p>
  <div class="about-btn">READ MORE</div>
  <svg class="foot-shape" viewBox="0 0 386 148"><path d="M0 20C130 10 270 14 386 52V148H0Z" fill="#1e1e20"/><path d="M140 13C250 16 330 32 386 50" fill="none" stroke="#0094D4" stroke-width="3"/></svg>
  <div class="foot-brand"><i></i><span>Tidewell Metrics Group</span></div>
  <a class="foot-nav" style="left:91px">HOME</a><a class="foot-nav" style="left:118px">CORE SERVICES</a><a class="foot-nav" style="left:167px">ABOUT US</a><a class="foot-nav" style="left:203px">OUR WORK</a><a class="foot-nav" style="left:242px">BLOG</a><a class="foot-nav" style="left:267px">CONTACT US</a>
  <i class="foot-ico" style="left:36px"><svg viewBox="0 0 6 6"><path d="M3 6C1 3.6 1 2.6 1 2a2 2 0 0 1 4 0c0 .6 0 1.6-2 4Z" fill="#ddd"/></svg></i>
  <span class="foot-text" style="left:51px">120 Harbor Line Rd NE<br>Suite 4 Atlanta, GA 30301</span>
  <i class="foot-ico" style="left:177px"><svg viewBox="0 0 6 6"><path d="M1 .5h1.3l.6 1.4-.8.6a3.5 3.5 0 0 0 1.4 1.4l.6-.8 1.4.6V5c-2.6.3-4.8-1.9-4.5-4.5Z" fill="#ddd"/></svg></i>
  <span class="foot-text" style="left:193px;top:1333px">404.555.0187</span>
  <i class="foot-ico" style="left:258px"><svg viewBox="0 0 6 6"><rect x=".5" y="1.2" width="5" height="3.6" fill="none" stroke="#ddd" stroke-width=".6"/><path d="M.5 1.2 3 3.2 5.5 1.2" fill="none" stroke="#ddd" stroke-width=".6"/></svg></i>
  <span class="foot-text" style="left:275px;top:1333px">info@tidewellmetrics.com</span>
  <i class="foot-soc" style="left:36px"></i><i class="foot-soc" style="left:51px"></i><i class="foot-soc" style="left:66px"></i>
  <span class="copyright">© 2022 Tidewell Metrics Group. All rights reserved</span>
</div>

<!-- PAGE 5 -->
<div class="page" style="left:1894px">
  <div class="topbar"><span class="tb-phone">☎ 404.555.0187</span><span class="tb-mail">✉ info@tidewellmetrics.com</span><i class="soc" style="left:160px"></i><i class="soc" style="left:168px"></i><i class="soc" style="left:176px"></i></div>
  <div class="brand"><i></i><span>Tidewell Metrics Group</span></div>
  <a class="nav active" style="left:133px">Home</a><a class="nav" style="left:156px">Core Services</a><a class="nav" style="left:197px">About Us</a><a class="nav" style="left:228px">Our Work</a><a class="nav" style="left:259px">Blog</a><a class="nav" style="left:279px">Contact Us</a>
  <div class="cta">GET STARTED</div>
  <div class="hero hero-5" role="img" aria-label="Blue sky above a sea of white clouds"></div>
  <div class="hero-title head">Tidewell Metrics Group</div>
  <div class="hero-sub head">Data Driven Research &amp; Insights</div>
  <i class="dot" style="left:190px;background:var(--blue)"></i><i class="dot" style="left:196px;background:var(--pale)"></i>
  <svg class="hero-curve" viewBox="0 0 386 65"><path d="M0 55C130 60 260 42 386 14V65H0Z" fill="#fff"/><path d="M160 54C250 48 330 34 386 12" fill="none" stroke="#0094D4" stroke-width="4"/></svg>
  <p class="eyebrow head">Welcome To</p>
  <h2 class="welcome-title head">Tidewell Metrics Group</h2>
  <p class="welcome-copy body-copy">Tidewell Metrics Group was formed in 2016 to help utilities and regulatory agencies navigate the technical, economic, and policy challenges of building a smarter and cleaner energy future. Through cutting edge research design and analysis methods we provide DSM program administrators with data-driven insights into how various technologies and interventions affect the way homes and businesses use energy.</p>
  <div class="welcome-btn btn-solid">READ MORE</div>
  <div class="ribbon" role="img" aria-label="Dotted blue ribbon graphic"></div>
  <div class="services">
    <i class="faint" style="left:2px;top:8px"></i><i class="faint" style="left:344px;top:135px"></i>
    <h2 class="section-title svc-title head">Our <b>Services</b></h2>
    <i class="arrow" style="left:14px"></i><i class="arrow" style="left:361px"></i>
    <div class="card blue" style="left:36px"><div class="card-img img-dash" role="img" aria-label="Analytics dashboard on a laptop"></div><span class="card-name">Predictive Analytics and Forecasting</span><span class="card-copy">Distributed energy resource integration into planning and operations</span><span class="card-btn">Read More</span></div>
    <div class="card grey" style="left:116px"><div class="card-img img-laptop" role="img" aria-label="Laptop showing data charts"></div><span class="card-name">T&amp;D Planning</span><span class="card-copy">Location specific, probabilistic forecasting for system-level T&amp;D planning</span><span class="card-btn">Read More</span></div>
    <div class="card blue" style="left:196px"><div class="card-img img-city" role="img" aria-label="City skyline with data overlay"></div><span class="card-name">Pilot &amp; Emerging Tech Support</span><span class="card-copy">Design and implementation of pilots and controlled deployments</span><span class="card-btn">Read More</span></div>
    <div class="card grey" style="left:277px"><div class="card-img img-tablet" role="img" aria-label="Tablet with analytics graphs"></div><span class="card-name">Program Portfolio &amp; Resource Planning</span><span class="card-copy">End-use load profile studies &amp; research baseline studies</span><span class="card-btn">Read More</span></div>
  </div>
  <h2 class="section-title pub-title head">Publications</h2><i class="underline"></i>
  <div class="pub-img" style="left:36px;top:686px" role="img" aria-label="Night city lights from above"></div>
  <h3 class="pub-head" style="left:209px;top:693px">Journal Articles and Conference Presentations</h3>
  <p class="pub-copy body-copy" style="left:209px;top:717px">Sed ut perspiciatis unde omnis iste natus error sit voluptatem accusantium doloremque laudantium, totam rem aperiam, eaque ipsa quae ab illo inventore veritatis et quasi architecto beatae vitae dicta sunt explicabo.</p>
  <div class="btn-outline" style="left:209px;top:760px">READ MORE</div>
  <h3 class="pub-head" style="left:47px;top:805px">Published Reports</h3>
  <p class="pub-copy body-copy" style="left:47px;top:819px">Sed ut perspiciatis unde omnis iste natus error sit voluptatem accusantium doloremque laudantium, totam rem aperiam, eaque ipsa quae ab illo inventore veritatis et quasi architecto beatae vitae dicta sunt explicabo.</p>
  <div class="btn-outline" style="left:47px;top:861px">READ MORE</div>
  <div class="pub-img chart" style="left:193px;top:785px" role="img" aria-label="Hand pointing at stock charts on a screen"></div>
  <h2 class="section-title team-title head">Our <b>Teams</b></h2>
  <div class="member" style="left:36px"><div class="avatar" role="img" aria-label="Portrait photo of team member"></div><span class="member-name">Marcus Hale, M.S.</span><span class="member-role">Partner</span><span class="member-bio">Marcus is an applied statistician whose work centers on estimating demand impacts.</span><i class="member-link"></i></div>
  <div class="member" style="left:118px"><div class="avatar warm" role="img" aria-label="Portrait photo of team member"></div><span class="member-name">Owen Prater, M.P.P.</span><span class="member-role">Partner</span><span class="member-bio">Owen specializes in novel applications of data analytics using large volumes of hourly data.</span><i class="member-link"></i></div>
  <div class="member" style="left:201px"><div class="avatar dark" role="img" aria-label="Portrait photo of team member"></div><span class="member-name">Lena Varga</span><span class="member-role">Partner</span><span class="member-bio">Lena's work has focused on distributed energy resources and solar photovoltaic systems.</span><i class="member-link"></i></div>
  <div class="member" style="left:283px"><div class="avatar dark" role="img" aria-label="Portrait photo of team member"></div><span class="member-name">Selma Ortiz, M.S.</span><span class="member-role">Partner</span><span class="member-bio">Selma has extensive expertise with analysis of smart meter data.</span><i class="member-link"></i></div>
  <div class="about"></div>
  <div class="about-img" role="img" aria-label="Desk with computer monitors showing analytics"></div>
  <h2 class="about-title head">About Us</h2>
  <p class="about-copy body-copy">Tidewell Metrics Group (TMG) was formed in 2016 to help utilities and regulatory agencies navigate the technical, economic, and policy challenges of building a smarter and cleaner energy future. Our research focuses on impact analysis as well as predictive &amp; causal analytics. We deliver data-driven insights into how various technologies and interventions affect the way homes and businesses use energy and how those in turn affect grid and system planning.</p>
  <div class="about-btn">READ MORE</div>
  <svg class="foot-shape" viewBox="0 0 386 148"><path d="M0 20C130 10 270 14 386 52V148H0Z" fill="#1e1e20"/><path d="M140 13C250 16 330 32 386 50" fill="none" stroke="#0094D4" stroke-width="3"/></svg>
  <div class="foot-brand"><i></i><span>Tidewell Metrics Group</span></div>
  <a class="foot-nav" style="left:91px">HOME</a><a class="foot-nav" style="left:118px">CORE SERVICES</a><a class="foot-nav" style="left:167px">ABOUT US</a><a class="foot-nav" style="left:203px">OUR WORK</a><a class="foot-nav" style="left:242px">BLOG</a><a class="foot-nav" style="left:267px">CONTACT US</a>
  <i class="foot-ico" style="left:36px"><svg viewBox="0 0 6 6"><path d="M3 6C1 3.6 1 2.6 1 2a2 2 0 0 1 4 0c0 .6 0 1.6-2 4Z" fill="#ddd"/></svg></i>
  <span class="foot-text" style="left:51px">120 Harbor Line Rd NE<br>Suite 4 Atlanta, GA 30301</span>
  <i class="foot-ico" style="left:177px"><svg viewBox="0 0 6 6"><path d="M1 .5h1.3l.6 1.4-.8.6a3.5 3.5 0 0 0 1.4 1.4l.6-.8 1.4.6V5c-2.6.3-4.8-1.9-4.5-4.5Z" fill="#ddd"/></svg></i>
  <span class="foot-text" style="left:193px;top:1333px">404.555.0187</span>
  <i class="foot-ico" style="left:258px"><svg viewBox="0 0 6 6"><rect x=".5" y="1.2" width="5" height="3.6" fill="none" stroke="#ddd" stroke-width=".6"/><path d="M.5 1.2 3 3.2 5.5 1.2" fill="none" stroke="#ddd" stroke-width=".6"/></svg></i>
  <span class="foot-text" style="left:275px;top:1333px">info@tidewellmetrics.com</span>
  <i class="foot-soc" style="left:36px"></i><i class="foot-soc" style="left:51px"></i><i class="foot-soc" style="left:66px"></i>
  <span class="copyright">© 2022 Tidewell Metrics Group. All rights reserved</span>
</div>

</div>
</body>
</html>
```